Social Movement/Church Plant Website - KindHearth.com

We need a website for our church plant startup, however we want the focus of the landing page to be around #kindhearth - that we are an organization that is FOR our town (Maplewood). The site will include serving project events, social events, a place to sign up for emails, a blog, a place to give, etc. All the elements we know we want are currently at kindhearth.com . Please check this for copy.

We want this to be easy to edit as a non-developer.

I have included several logos with our colors, as well as an ai file to give you an idea of how we want the design to look and feel - also includes our branded fonts

Target Market(s)

People who live in the Northern CO area

Font styles to use
Serif
Sans Serif

Requirements
Must have
• Events (serve and social), Blog section, A place to get involved - where to give and to sign up for emails. Must match our branding colors and style hex 4c7991.
Should not have
• Should not be focused on the actual church plant on the home page. There can be some back end stuff about it, but the focus should be #kindhearth.

```html
<!DOCTYPE html>
<html lang="en">
<head>
<meta charset="utf-8">
<title>For Maplewood — Cedar Hollow Church</title>
<link rel="stylesheet" href="https://fonts.googleapis.com/css2?family=Abril+Fatface&family=Lato:ital,wght@0,400;0,700;1,400&family=Playfair+Display:ital@1&display=swap">
<style>
  :root {
    --brand: #4c7991;
    --slate: #5b6f7f;
    --slate-dark: #3f4c57;
    --ink: #2f3a42;
    --body: #6b7278;
    --paper: #ffffff;
    --mist: #eeeeee;
    --line: #d9dde0;
  }
  * { box-sizing: border-box; margin: 0; padding: 0; }
  html, body { width: 1200px; height: 3732px; overflow: hidden; }
  body { position: relative; background: var(--paper); font-family: "Lato", Arial, sans-serif; color: var(--body); }
  .abs { position: absolute; }
  .serif { font-family: "Abril Fatface", Georgia, serif; font-weight: 400; }

  .topbar { left: 0; top: 0; width: 1200px; height: 32px; background: var(--slate-dark); color: #fff; font-size: 13px; font-weight: 700; letter-spacing: 1px; display: flex; justify-content: flex-end; align-items: center; padding-right: 60px; gap: 10px; }
  .topbar svg { width: 14px; height: 14px; }
  .header { left: 0; top: 32px; width: 1200px; height: 108px; background: var(--paper); }
  .brand-name { left: 72px; top: 22px; color: var(--slate); text-align: center; line-height: 1; }
  .brand-name .l1 { font-family: "Abril Fatface", Georgia, serif; font-size: 34px; letter-spacing: 2px; display: block; }
  .brand-name .l2 { font-family: "Abril Fatface", Georgia, serif; font-size: 18px; letter-spacing: 9px; display: block; margin-top: 4px; }
  .nav { right: 60px; top: 52px; display: flex; gap: 30px; font-size: 14px; color: var(--ink); letter-spacing: .5px; }

  .hero { left: 0; top: 140px; width: 1200px; height: 700px; background: linear-gradient(180deg,#8fb1cf 0%,#b7c7d3 28%,#6f7e88 45%,#2f4a3b 62%,#22382c 78%,#3c5f7a 90%,#2d4b63 100%); clip-path: polygon(0 0,100% 0,100% 660px,50% 700px,0 660px); }
  .hero-title { left: 0; top: 350px; width: 1200px; text-align: center; color: #fff; font-size: 72px; letter-spacing: 2px; }
  .hero-sub { left: 0; top: 450px; width: 1200px; text-align: center; color: #fff; font-size: 28px; font-weight: 700; letter-spacing: 2px; }

  .h-section { color: var(--ink); font-size: 46px; letter-spacing: 1px; }
  .story-head { left: 72px; top: 880px; }
  .story-sub { left: 72px; top: 944px; font-family: "Playfair Display", Georgia, serif; font-style: italic; font-size: 22px; color: var(--slate); }
  .story-text { left: 72px; top: 990px; width: 380px; font-size: 14px; line-height: 22px; }
  .story-text p + p { margin-top: 14px; }
  .btn { display: inline-flex; align-items: center; justify-content: center; height: 46px; padding: 0 22px; font-size: 15px; font-weight: 700; letter-spacing: 1px; background: var(--slate); color: #fff; }
  .btn-outline { background: var(--paper); color: var(--slate); border: 2px solid var(--slate); }
  .story-actions { left: 72px; top: 1270px; display: flex; gap: 14px; }
  .story-frame { left: 610px; top: 880px; width: 380px; height: 440px; border: 6px solid var(--brand); }
  .photo { border: 5px solid #fff; box-shadow: 0 2px 8px rgba(0,0,0,.25); }
  .ph-sod { left: 628px; top: 832px; width: 316px; height: 352px; background: linear-gradient(160deg,#b9c1b7,#6a7a48 55%,#7b5b3b); }
  .ph-gardener { left: 884px; top: 1010px; width: 192px; height: 200px; background: linear-gradient(170deg,#8bb36a,#3f6a35 60%,#2c4a2a); }
  .ph-shrubs { left: 752px; top: 1200px; width: 250px; height: 210px; background: linear-gradient(160deg,#9cc25a,#4f7a32 60%,#2d4a22); }

  .events { left: 0; top: 1480px; width: 1200px; height: 600px; background: linear-gradient(180deg,#4a5a66 0%,#2f3c45 45%,#25323b 100%); }
  .h-light { color: #fff; }
  .events-head { left: 0; top: 1530px; width: 1200px; text-align: center; }
  .card { top: 1610px; width: 320px; height: 340px; background: #fff; padding: 10px; text-align: center; }
  .card .img { height: 210px; }
  .card .title { margin-top: 18px; font-size: 18px; color: var(--ink); }
  .card .date { margin-top: 6px; font-size: 12px; color: var(--body); }
  .card .btn { margin-top: 12px; height: 34px; font-size: 12px; padding: 0 16px; }
  .pager { display: flex; align-items: center; gap: 14px; left: 0; width: 1200px; justify-content: center; }
  .pager .dot { width: 12px; height: 12px; border-radius: 50%; border: 2px solid currentColor; }
  .pager .dot.on { background: currentColor; }
  .pager svg { width: 22px; height: 14px; }

  .blog-head { left: 0; top: 2098px; width: 1200px; text-align: center; }
  .blog-row { left: 76px; top: 2160px; width: 1048px; height: 260px; display: grid; grid-template-columns: 262px 262px 262px 262px; }
  .blog-text { background: var(--mist); padding: 36px 28px; font-size: 13px; line-height: 20px; }
  .blog-text .date { text-align: right; margin-bottom: 12px; }
  .blog-text .more { margin-top: 14px; font-weight: 700; font-size: 12px; color: var(--ink); text-decoration: underline; }

  .testimonials { left: 0; top: 2560px; width: 1200px; height: 360px; background: linear-gradient(135deg,#1f2f1f,#3c5233 50%,#232e22); }
  .testi-head { left: 0; top: 2582px; width: 1200px; text-align: center; }
  .avatar { left: 546px; top: 2664px; width: 108px; height: 108px; border-radius: 50%; border: 4px solid #fff; background: linear-gradient(160deg,#9fb0bd,#5c6f7c); }
  .testi-text { left: 210px; top: 2800px; width: 780px; text-align: center; color: #fff; font-size: 14px; line-height: 21px; }
  .testi-name { left: 0; top: 2880px; width: 1200px; text-align: center; color: #fff; font-size: 13px; font-weight: 700; letter-spacing: 1px; }
  .side-arrow { top: 2816px; width: 26px; height: 26px; }

  .partner-head { left: 0; top: 3068px; width: 1200px; text-align: center; font-family: "Abril Fatface", Georgia, serif; font-size: 38px; color: var(--slate-dark); }
  .partner-sub { left: 0; top: 3130px; width: 1200px; text-align: center; font-size: 16px; }
  .partner-actions { left: 0; top: 3196px; width: 1200px; display: flex; justify-content: center; gap: 16px; }
  .partner-actions .btn { width: 180px; }

  .newsletter { left: 0; top: 3320px; width: 1200px; height: 340px; background: linear-gradient(180deg,#3d4a36,#253123 60%,#33472a); clip-path: polygon(0 0,50% 40px,100% 0,100% 100%,0 100%); }
  .socials { left: 0; top: 3418px; width: 1200px; display: flex; justify-content: center; gap: 18px; }
  .socials span { width: 44px; height: 44px; border-radius: 50%; border: 2px solid #fff; }
  .news-head { left: 0; top: 3488px; width: 1200px; text-align: center; color: #fff; font-size: 34px; }
  .news-form { left: 352px; top: 3560px; width: 496px; height: 48px; display: flex; }
  .news-form .field { flex: 1; border: 2px solid #fff; border-radius: 24px 0 0 24px; border-right: 0; color: #e7ecef; font-size: 14px; display: flex; align-items: center; padding-left: 22px; }
  .news-form .submit { width: 130px; background: #fff; border-radius: 24px; color: var(--ink); font-weight: 700; font-size: 14px; letter-spacing: 1px; display: flex; align-items: center; justify-content: center; }

  .footer { left: 0; top: 3660px; width: 1200px; height: 72px; background: var(--brand); color: #fff; font-size: 13px; display: flex; align-items: center; justify-content: center; letter-spacing: .5px; }
</style>
</head>
<body>

<div class="abs topbar">CALL US NOW
  <svg viewBox="0 0 24 24" fill="#fff"><path d="M6.6 10.8a15 15 0 0 0 6.6 6.6l2.2-2.2a1 1 0 0 1 1-.25 11.4 11.4 0 0 0 3.6.6 1 1 0 0 1 1 1V20a1 1 0 0 1-1 1A17 17 0 0 1 3 4a1 1 0 0 1 1-1h3.5a1 1 0 0 1 1 1c0 1.25.2 2.45.6 3.6a1 1 0 0 1-.25 1z"/></svg>
  (123) 456 7890</div>
<header class="abs header">
  <div class="abs brand-name"><span class="l1">CEDAR HOLLOW</span><span class="l2">CHURCH</span></div>
  <nav class="abs nav"><span>HOME</span><span>ABOUT</span><span>EVENTS</span><span>BLOG</span><span>GIVE</span><span>CONTACT US</span></nav>
</header>

<section class="abs hero" role="img" aria-label="Mountain range above a pine forest and a lake"></section>
<h1 class="abs hero-title serif">FOR MAPLEWOOD</h1>
<div class="abs hero-sub">CEDAR HOLLOW CHURCH</div>

<h2 class="abs story-head h-section serif">OUR STORY</h2>
<div class="abs story-sub">Working Toward a Better Tomorrow.</div>
<div class="abs story-text">
  <p>What if we were known not by what we're against, but by what we're for? If our collective energy was invested in things that unite rather than divide, wouldn't we see stronger neighborhoods, healthier communities, and more resilient relationships? We believe so.</p>
  <p>We are for the broken and the brand new, the beautifully patched and the terribly stuck. We are for the skilled and the unsure, the put-together and the never-been-anywhere. We are for families and individuals, for the outcast and the unnoticed.</p>
</div>
<div class="abs story-actions"><span class="btn">KNOW MORE</span><span class="btn btn-outline">CONTACT US</span></div>
<div class="abs story-frame"></div>
<div class="abs photo ph-sod" role="img" aria-label="Hands rolling out fresh sod"></div>
<div class="abs photo ph-gardener" role="img" aria-label="Volunteer gardener planting"></div>
<div class="abs photo ph-shrubs" role="img" aria-label="Freshly planted shrubs in a garden bed"></div>

<section class="abs events" role="img" aria-label="Dark mountain landscape background"></section>
<h2 class="abs events-head h-section h-light serif">UPCOMING EVENTS</h2>
<div class="abs card" style="left:76px"><div class="img" role="img" aria-label="Volunteer watering a garden" style="background:linear-gradient(160deg,#9fcf72,#3f7a34)"></div><div class="title">Lorem Ipsum is simply dummy.</div><div class="date">11 DEC 2018</div><span class="btn">KNOW MORE</span></div>
<div class="abs card" style="left:440px"><div class="img" role="img" aria-label="Purple wildflowers below snowy peaks" style="background:linear-gradient(180deg,#7fb3e0,#d9e6f0 40%,#6a4fb0 70%,#3b2d73)"></div><div class="title">Lorem Ipsum is simply dummy.</div><div class="date">11 DEC 2018</div><span class="btn">KNOW MORE</span></div>
<div class="abs card" style="left:804px"><div class="img" role="img" aria-label="Outdoor patio table set for a gathering" style="background:linear-gradient(160deg,#7a8c5a,#b5a37a 50%,#5a4632)"></div><div class="title">Lorem Ipsum is simply dummy.</div><div class="date">11 DEC 2018</div><span class="btn">KNOW MORE</span></div>
<div class="abs pager" style="top:2004px;color:#fff">
  <svg viewBox="0 0 22 14"><path d="M21 7H2M8 1 2 7l6 6" fill="none" stroke="currentColor" stroke-width="2"/></svg>
  <span class="dot on"></span><span class="dot"></span><span class="dot"></span>
  <svg viewBox="0 0 22 14"><path d="M1 7h19M14 1l6 6-6 6" fill="none" stroke="currentColor" stroke-width="2"/></svg>
</div>

<h2 class="abs blog-head h-section serif">RECENT BLOG POST</h2>
<div class="abs blog-row">
  <div role="img" aria-label="Volunteer trimming a hedge" style="background:linear-gradient(160deg,#8cbf5a,#3e6d2c)"></div>
  <div class="blog-text"><div class="date">October 20, 2018</div>Lorem Ipsum is simply dummy text of the printing and typesetting industry. Lorem Ipsum has been the industry.<div class="more">READ MORE</div></div>
  <div role="img" aria-label="Child holding a sunflower" style="background:linear-gradient(160deg,#9fc8e8,#e8c94a 55%,#6c8a3a)"></div>
  <div class="blog-text"><div class="date">October 20, 2018</div>Lorem Ipsum is simply dummy text of the printing and typesetting industry. Lorem Ipsum has been the industry.<div class="more">READ MORE</div></div>
</div>
<div class="abs pager" style="top:2460px;color:var(--ink)">
  <svg viewBox="0 0 22 14"><path d="M21 7H2M8 1 2 7l6 6" fill="none" stroke="currentColor" stroke-width="2"/></svg>
  <span class="dot on"></span><span class="dot"></span><span class="dot"></span>
  <svg viewBox="0 0 22 14"><path d="M1 7h19M14 1l6 6-6 6" fill="none" stroke="currentColor" stroke-width="2"/></svg>
</div>

<section class="abs testimonials" role="img" aria-label="Hands planting a seedling in soil"></section>
<h2 class="abs testi-head h-section h-light serif">TESTIMONIALS</h2>
<div class="abs avatar" role="img" aria-label="Portrait of the person giving the testimonial"></div>
<p class="abs testi-text">Lorem Ipsum is simply dummy text of the printing and typesetting industry. Lorem Ipsum has been the industry's standard dummy text ever since the 1500s, when an unknown printer took a galley of type and scrambled it to make a type specimen book. It has survived not only five centuries, but also the leap into electronic typesetting, remaining essentially unchanged.</p>
<div class="abs testi-name">- NAME SURNAME -</div>
<svg class="abs side-arrow" style="left:70px" viewBox="0 0 26 26"><path d="M17 3 7 13l10 10" fill="none" stroke="#fff" stroke-width="3"/></svg>
<svg class="abs side-arrow" style="left:1104px" viewBox="0 0 26 26"><path d="m9 3 10 10-10 10" fill="none" stroke="#fff" stroke-width="3"/></svg>

<h2 class="abs partner-head">Interested in Partnering With Us?</h2>
<p class="abs partner-sub">We would love to partner with you to help in our community!</p>
<div class="abs partner-actions"><span class="btn">GET INVOLVED</span><span class="btn">PARTNERSHIP</span><span class="btn">DONATE</span></div>

<section class="abs newsletter" role="img" aria-label="Green lawn and garden at dusk"></section>
<div class="abs socials"><span></span><span></span><span></span></div>
<h2 class="abs news-head serif">Join our mailing list and stay updated!</h2>
<div class="abs news-form"><div class="field">Enter Your email</div><div class="submit">SUBSCRIBE</div></div>

<footer class="abs footer">©CEDAR HOLLOW CHURCH. 2018 - All Rights Reserved.</footer>

</body>
</html>
```